Calm Ridge is a new opened business in takapuna, Auckland, which provide traditional Chinese Therapeutic & relaxation massage. We like to invite more and more people as our customers, especially for the office people near by in the same suburb. We want this flyer to have a pormotion for these kind of people,the probably content of this pormotion is during their lunch break, they will receive a professional Quckily De-stress Relaxation massage for $20 only. We are not the native speaker so we wouldn't use specific sentence to describe. We like the ad be academic and professional.The color we want to use is the same as the file we have attached.also in the flyer we need the direction for the location of our shop.
Industry/Entity Type
Massage
Requirements
Must have
- have a pormotion for office people,the probably content of this pormotion is during their lunch break, they will receive a professional Quckily De-stress Relaxation massage for $20 only.
Nice to have
- our shop address is shop 7, 15 - 29 Pellowan Street, Takapuna, Auckland.
Phone number: 09-5172038
Email: calmridge.nz@brelvio.com
we need the direction for the location of our shop (map)

```html
<!DOCTYPE html>
<html lang="en">
<head>
<meta charset="utf-8">
<title>Calm Ridge – Lunch Break Massage Flyer</title>
<link rel="stylesheet" href="https://fonts.googleapis.com/css2?family=Roboto+Condensed:wght@300;400&family=Arimo:wght@400;700&display=swap">
<style>
  :root {
    --stage: #2f2f2f;
    --wine-dark: #3d0508;
    --wine: #7a0d15;
    --wine-bright: #9c1420;
    --brown-band: #5a2b26;
    --burst: #5e2a27;
    --gold: #d9a64a;
    --gold-light: #f0d08a;
    --cream: #ffffff;
    --ink: #222222;
    --skin-warm: #c98d72;
    --photo-dark: #4a2a22;
    --map-paper: #ecebe6;
    --map-road: #f2c25a;
  }
  * { margin: 0; padding: 0; box-sizing: border-box; }
  html, body { width: 1200px; height: 900px; overflow: hidden; }
  body {
    background: var(--stage);
    position: relative;
    font-family: "Arimo", Arial, sans-serif;
  }
  .flyer {
    position: absolute;
    top: 85px;
    width: 513px;
    height: 730px;
    overflow: hidden;
    box-shadow: 0 4px 14px rgba(0,0,0,0.5);
  }
  .flyer--front { left: 73px; background: var(--cream); }
  .flyer--back {
    left: 616px;
    background: linear-gradient(160deg, var(--wine-bright) 0%, var(--wine) 40%, var(--wine-dark) 100%);
    color: var(--cream);
  }

  /* Front */
  .hero-photo {
    position: absolute; left: 0; top: 0; width: 513px; height: 632px;
    background:
      radial-gradient(ellipse 45% 55% at 62% 45%, var(--skin-warm) 0%, #a8705a 55%, transparent 80%),
      linear-gradient(135deg, #8a4a44 0%, var(--photo-dark) 45%, #6a4034 100%);
  }
  .offer-burst {
    position: absolute; left: 0; top: 145px; width: 220px; height: 220px;
  }
  .offer-burst svg { position: absolute; inset: 0; }
  .offer-text {
    position: absolute; left: 18px; top: 38px; width: 190px;
    color: var(--cream);
    transform: rotate(-22deg);
    text-align: right;
    font-family: "Arimo", Arial, sans-serif;
  }
  .offer-lead {
    font-size: 13px; line-height: 15px; letter-spacing: 0.3px; text-transform: uppercase;
    padding-right: 6px;
  }
  .offer-price {
    font-family: "Roboto Condensed", Arial, sans-serif;
    font-weight: 300; font-size: 72px; line-height: 70px; text-align: left; padding-left: 20px;
  }
  .brand {
    position: absolute;
    display: flex; flex-direction: column; align-items: center;
    transform: translateX(-50%);
  }
  .brand-row { display: flex; align-items: center; gap: 8px; }
  .brand-dot { width: 14px; height: 14px; border-radius: 50%; background: var(--gold); }
  .brand-name {
    font-family: "Arimo", Arial, sans-serif; font-weight: 700; font-size: 34px; line-height: 38px;
  }
  .brand-tagline {
    font-family: "Arimo", Arial, sans-serif; font-weight: 700; font-size: 9.5px;
    text-transform: uppercase; letter-spacing: 0.3px; line-height: 11px; text-align: center; margin-top: 2px;
  }
  .flyer--front .brand { left: 237px; top: 530px; color: var(--cream); }
  .service-band {
    position: absolute; left: 0; top: 632px; width: 513px; height: 56px;
    background: var(--brown-band);
    color: var(--cream);
    font-family: "Roboto Condensed", Arial, sans-serif; font-weight: 300;
    font-size: 16.5px; letter-spacing: 0.5px;
    display: flex; align-items: center; padding-left: 21px;
  }
  .contact-strip {
    position: absolute; left: 0; top: 688px; width: 513px; height: 42px;
    display: flex; align-items: center; justify-content: space-between;
    padding: 0 18px 0 18px; color: var(--ink);
  }
  .contact-strip .address { font-size: 11px; }
  .contact-strip .phone {
    font-family: "Roboto Condensed", Arial, sans-serif; font-weight: 300; font-size: 29px;
  }

  /* Back */
  .headline {
    position: absolute; left: 32px; top: 22px;
    font-family: "Roboto Condensed", Arial, sans-serif; font-weight: 300;
    letter-spacing: -0.5px;
  }
  .headline-top { display: block; font-size: 55px; line-height: 62px; }
  .headline-main { display: block; font-size: 74px; line-height: 74px; }
  .headline-rule {
    position: absolute; left: 32px; top: 157px; width: 468px; height: 1px;
    background: rgba(255,255,255,0.7);
  }
  .benefit { position: absolute; font-size: 10.8px; line-height: 13.5px; }
  .benefit h2 {
    font-family: "Arimo", Arial, sans-serif; font-weight: 700; font-size: 17.5px; line-height: 22px;
    margin-bottom: 6px;
  }
  .benefit p { margin-bottom: 5px; }
  .benefit--sports { left: 33px; top: 180px; width: 180px; }
  .benefit--remedial { left: 266px; top: 180px; width: 200px; }
  .benefit--relax { left: 0; top: 384px; width: 513px; text-align: center; font-size: 11.5px; }
  .benefit--relax p { margin-bottom: 7.5px; }
  .gold-band {
    position: absolute; left: 0; top: 551px; width: 513px; height: 6px;
    background: linear-gradient(90deg, var(--gold) 0%, var(--gold-light) 50%, var(--gold) 100%);
  }
  .flyer--back .brand { left: 280px; top: 565px; color: var(--cream); }
  .flyer--back .brand-name { font-size: 30px; line-height: 34px; }
  .location-map {
    position: absolute; left: 0; top: 557px; width: 234px; height: 173px;
    background: linear-gradient(135deg, var(--map-paper) 0%, #dedcd4 60%, var(--map-paper) 100%);
  }
  .back-contact {
    position: absolute; right: 32px; top: 620px; text-align: right;
  }
  .back-contact .phone {
    font-family: "Roboto Condensed", Arial, sans-serif; font-weight: 300; font-size: 31px; line-height: 34px;
  }
  .back-contact .address { font-size: 13.5px; line-height: 16px; margin-top: 4px; }
  .back-contact .email { font-size: 9.5px; margin-top: 14px; }
</style>
</head>
<body>

  <section class="flyer flyer--front">
    <div class="hero-photo" role="img" aria-label="Photo of a woman relaxing with eyes closed while receiving a head massage, surrounded by spa stones, bath salts and a pink lily"></div>

    <div class="offer-burst">
      <svg viewBox="0 0 220 220" width="220" height="220" aria-hidden="true">
        <polygon fill="var(--burst)" fill-opacity="0.92" points="216,110 196.9,133.3 201.8,163 173.6,173.6 163,201.8 133.3,196.9 110,216 86.7,196.9 57,201.8 46.4,173.6 18.2,163 23.1,133.3 4,110 23.1,86.7 18.2,57 46.4,46.4 57,18.2 86.7,23.1 110,4 133.3,23.1 163,18.2 173.6,46.4 201.8,57 196.9,86.7"/>
      </svg>
      <div class="offer-text">
        <div class="offer-lead">Professional<br>Quckily De-stress<br>Relaxation<br>Massage for</div>
        <div class="offer-price">$20</div>
      </div>
    </div>

    <div class="brand">
      <div class="brand-row"><span class="brand-dot"></span><span class="brand-name">Calm Ridge</span></div>
      <div class="brand-tagline">Professional Therapeutic<br>&amp; Relaxation Massage</div>
    </div>

    <div class="service-band">TRADITIONAL CHINESE THERAPEUTIC &amp; RELAXATION MASSAGE</div>
    <div class="contact-strip">
      <span class="address">Shop 7, 15 - 29 Pellowan Street, Takapuna, Auckland</span>
      <span class="phone">09-5172038</span>
    </div>
  </section>

  <section class="flyer flyer--back">
    <h1 class="headline">
      <span class="headline-top">How does a Massage</span>
      <span class="headline-main">BENEFIT US?</span>
    </h1>
    <div class="headline-rule"></div>

    <div class="benefit benefit--sports">
      <h2>Sports massage</h2>
      <p>Remain injury free &amp; improve your performance by assisting muscles back to their normal resting length therefore improving strength and flexibility.</p>
      <p>Deep tissue massage to realign muscle fibres and eliminate trigger points.</p>
      <p>Speed up your recovery between training sessions and events by flushing out metabolic waste.</p>
    </div>

    <div class="benefit benefit--remedial">
      <h2>Therapeutic/<br>remedial massage</h2>
      <p>Reduce the incidence of headaches and migraines.</p>
      <p>Resolve your lower back pain.</p>
      <p>Improve your posture and become pain-free.</p>
      <p>Eliminate "mouse" shoulder and neck pain from poor desk posture.</p>
      <p>Eliminate referral pain such as Sciatica and arm pain.</p>
    </div>

    <div class="benefit benefit--relax">
      <h2>Relaxation massage</h2>
      <p>Scheduled time-out for you.</p>
      <p>De-stress and reduce your muscle tension.</p>
      <p>Quieten your mind and assist in a good night's sleep.</p>
    </div>

    <div class="gold-band"></div>
    <div class="location-map" role="img" aria-label="Street map of Takapuna showing the way to the shop on Pellowan Street"></div>

    <div class="brand">
      <div class="brand-row"><span class="brand-dot"></span><span class="brand-name">Calm Ridge</span></div>
      <div class="brand-tagline">Professional Therapeutic<br>&amp; Relaxation Massage</div>
    </div>

    <div class="back-contact">
      <div class="phone">09-5172038</div>
      <div class="address">Shop 7, 15 - 29 Pellowan Street<br>Takapuna, Auckland</div>
      <div class="email">calmridge.nz@brelvio.com</div>
    </div>
  </section>

</body>
</html>
```